Gymnastics equipment catalogue

I have up to 4 pages to fill with gymnastics, sensory and flexible learning space equipment pictures and info. This will go in a 300 page sporting goods catalogue.
I would like the types of equipment separated into categories. I will need to give you additional pics and info. Too tricky to upload some of the pics.
I have an example that will show exactly what I want, but it won't upload. Happy to swap emails

Target Market(s)

School phys ed and special needs teachers

Industry/Entity Type

Sporting Good

Font styles to use
Sans Serif

Colors
3176b5
34a6d7
33b8a4
acd036
fbee3d
9bcb3c
876aae
e667a6

Requirements
Must have
• Pictures and prices and some info.
• I have alot more pictures and info. Finding it tricky to upload them. can email

```html
<!DOCTYPE html>
<html lang="en">
<head>
<meta charset="utf-8">
<title>Gymnastics Equipment Catalogue</title>
<link href="https://fonts.googleapis.com/css2?family=Montserrat:wght@400;500;600;700&family=Oswald:wght@300;600&display=swap" rel="stylesheet">
<style>
:root{
  --stage:#3b3b3c;
  --paper:#f5f6f6;
  --navy:#1d3b6c;
  --blue:#3176b5;
  --sky:#34a6d7;
  --teal:#33b8a4;
  --lime:#acd036;
  --green:#9bcb3c;
  --yellow:#fbee3d;
  --purple:#876aae;
  --pink:#e667a6;
  --red:#e63a2e;
  --orange:#f18a23;
  --ink:#222;
  --text:#444;
}
*{margin:0;padding:0;box-sizing:border-box}
html,body{width:847px;height:1200px;overflow:hidden}
body{background:var(--stage);font-family:"Montserrat",sans-serif;color:var(--text);position:relative}
.page{position:absolute;overflow:hidden;background:linear-gradient(160deg,#fff 0%,var(--paper) 55%,#eceeee 100%)}
.page--cover{left:47px;top:55px;width:369px;height:521px;background:#fff}
.page--contact{left:431px;top:55px;width:369px;height:521px}
.page--left{left:47px;top:594px;width:371px;height:525px}
.page--right{left:430px;top:594px;width:371px;height:525px}
.abs{position:absolute}
.band{position:absolute;left:0;right:0;bottom:0;height:22px;background:var(--teal);color:#fff;font-size:7.5px;font-weight:600;display:flex;align-items:center;padding:0 22px}
.band--right{justify-content:flex-end}
.wordmark{position:absolute;background:var(--navy);color:#fff;display:flex;align-items:center;justify-content:center;font-family:"Montserrat",sans-serif;font-weight:700;font-size:20px;letter-spacing:2px;width:117px;height:47px}
.cover-title{position:absolute;left:138px;top:362px;font-family:"Oswald",sans-serif;line-height:1}
.cover-title__main{display:block;color:var(--teal);font-weight:600;font-size:38px;letter-spacing:-.5px}
.cover-title__sub{display:block;color:#222;font-weight:300;font-size:23px;margin-top:2px;letter-spacing:-.4px}
.photo{position:absolute;border-radius:4px}
.photo--blue{background:radial-gradient(ellipse at 40% 40%,#5d8fd6,#2d5fae 80%)}
.photo--red{background:radial-gradient(ellipse at 40% 40%,#f0554a,#cf2f26 80%)}
.photo--green{background:radial-gradient(ellipse at 40% 40%,#8fcd55,#5ea234 80%)}
.photo--dark{background:radial-gradient(ellipse at 50% 40%,#3a3a3a,#1c1c1c 80%)}
.photo--multi{background:linear-gradient(135deg,#4a8fd0,#e0a84a 50%,#e2504a)}
.photo--wood{background:radial-gradient(ellipse at 50% 50%,#d5b48a,#b98e5c 85%)}
.photo--purple{background:radial-gradient(ellipse at 40% 40%,#a08ac4,#7a5fa3 85%)}
.card{position:absolute;background:rgba(255,255,255,.82);border-radius:5px;box-shadow:0 1px 4px rgba(0,0,0,.13);padding:8px 12px}
.card h3{font-size:9.5px;font-weight:600;color:var(--ink);margin-bottom:4px}
.card p{font-size:5.6px;line-height:1.45;text-align:justify}
.card ul{list-style:none;font-size:5.2px;line-height:1.45}
.card ul li::before{content:"• "}
.card .dims{font-size:6.6px;font-weight:600;color:var(--ink);margin-bottom:2px}
.card--right h3,.card--right p{text-align:right}
.card--center h3,.card--center p{text-align:center}
.label{position:absolute;font-size:9px;font-weight:600;color:var(--ink);text-align:center}
.desc{position:absolute;font-size:5.6px;line-height:1.45;text-align:center}
.desc h3{font-size:9.5px;font-weight:600;color:var(--ink);margin-bottom:3px}
.footnote{position:absolute;font-size:3.9px;line-height:1.4;color:#555}
.contact{position:absolute;left:31px;top:334px;width:306px;height:81px;background:#fff;border-radius:5px;box-shadow:0 1px 5px rgba(0,0,0,.14)}
.contact .wordmark{left:10px;top:17px}
.contact__rule{position:absolute;left:139px;top:14px;width:1px;height:53px;background:#cfcfcf}
.contact__list{position:absolute;left:150px;top:14px;list-style:none}
.contact__list li{display:flex;align-items:center;height:19px;color:var(--ink);font-weight:600}
.contact__list li svg{width:12px;height:12px;margin-right:7px;flex:none}
.contact__phone{font-size:9.5px}
.contact__addr,.contact__mail{font-size:6.4px}
.section-head{position:absolute;top:18px;height:34px}
.section-head text{font-family:"Montserrat",sans-serif;font-weight:700;fill:#fff}
.ninja-sub{font-size:5.8px;font-weight:700;color:var(--ink);text-decoration:underline;margin:4px 0 2px}
.ninja-sub2{font-size:5.8px;font-weight:700;color:var(--ink);margin:5px 0 2px}
.card--ninja p{font-size:4.9px;line-height:1.35;text-align:left}
.beam-caption{position:absolute;font-size:5.6px;font-weight:600;color:var(--ink);line-height:1.3}
</style>
</head>
<body>

<section class="page page--cover">
  <svg class="abs" style="left:0;top:0" width="369" height="521" viewBox="0 0 461 651">
    <polygon points="300,80 461,0 461,240" fill="#e9f4e0" opacity=".7"/>
    <polygon points="350,150 461,260 350,370 240,260" fill="#eef0f0"/>
    <polygon points="400,300 461,360 461,480 380,400" fill="#e5f1d6"/>
    <polygon points="0,0 170,0 170,150 0,300" fill="#8aa0b8" role="img" aria-label="Photo of a child sitting on soft play blocks using a laptop"/>
    <polygon points="170,150 230,150 230,195 175,250" fill="var(--teal)"/>
    <polygon points="0,270 140,400 0,540" fill="var(--blue)"/>
    <polygon points="0,420 160,540 100,620 0,651" fill="var(--green)"/>
    <polygon points="100,540 250,540 175,620" fill="#cfe5a4"/>
    <polygon points="0,560 60,620 0,651" fill="#7fb23a"/>
    <polygon points="173,136 311,286 173,436 36,286" fill="#3f6fb7" role="img" aria-label="Photo of a young girl standing on blue gymnastics mats"/>
  </svg>
  <div class="wordmark" style="left:186px;top:60px">VAULTA</div>
  <h1 class="cover-title">
    <span class="cover-title__main">GYMNASTICS</span>
    <span class="cover-title__sub">EQUIPMENT CATALOGUE</span>
  </h1>
  <div class="photo photo--dark" role="img" aria-label="Photo of a mini trampoline" style="left:140px;top:437px;width:105px;height:68px"></div>
  <div class="photo photo--multi" role="img" aria-label="Photo of a foam vault box" style="left:262px;top:444px;width:46px;height:60px"></div>
  <div class="photo photo--multi" role="img" aria-label="Photo of a foam vault box" style="left:320px;top:444px;width:49px;height:60px"></div>
  <div class="band"></div>
</section>

<section class="page page--contact">
  <div class="photo photo--wood" role="img" aria-label="Photo of a timber balance beam" style="left:22px;top:118px;width:131px;height:34px"></div>
  <article class="card" style="left:177px;top:87px;width:168px;height:82px">
    <h3>Balance Beam</h3>
    <p>Club and school gymnastics balance beam, 3m in length, with a regulation 10cm working surface. 20cm height. Lightweight Aluminium construction, with convex sides as per competition balance beams</p>
  </article>
  <article class="card" style="left:22px;top:205px;width:168px;height:84px">
    <h3>Spring board</h3>
    <p>Competition Springboard (Soft version) Competition standard, 120x60x22 cm, with 7 HDI tapered Springs</p>
    <p>Spring board for kids Just for kids, dimension 50×76×16cm, made of high quality—plywood, sponge and carpets. Only 2 springs.</p>
  </article>
  <div class="photo photo--red" role="img" aria-label="Photo of a red carpeted springboard" style="left:206px;top:220px;width:140px;height:62px"></div>
  <div class="contact">
    <div class="wordmark">VAULTA</div>
    <div class="contact__rule"></div>
    <ul class="contact__list">
      <li class="contact__phone"><svg viewBox="0 0 12 12"><circle cx="6" cy="6" r="5.2" fill="none" stroke="var(--teal)" stroke-width="1.1"/><path d="M4 3.3l1.1 1.2-.6.8c.4.8 1 1.4 1.8 1.8l.8-.6 1.2 1.1-.7 1c-2.2-.3-4.2-2.3-4.5-4.5z" fill="var(--teal)"/></svg>+61 3 9000 4182</li>
      <li class="contact__addr"><svg viewBox="0 0 12 12"><path d="M6 1a3.6 3.6 0 0 0-3.6 3.6C2.4 7.4 6 11 6 11s3.6-3.6 3.6-6.4A3.6 3.6 0 0 0 6 1z" fill="var(--teal)"/><circle cx="6" cy="4.6" r="1.3" fill="#fff"/></svg>12 Carrow St NORTHBY VIC 3000</li>
      <li class="contact__mail"><svg viewBox="0 0 12 12"><rect x="1" y="3" width="10" height="7" fill="var(--teal)"/><path d="M1 3l5 4 5-4" fill="none" stroke="#fff" stroke-width=".8"/></svg>sales@vaultasports.com.au</li>
    </ul>
  </div>
  <div class="band"></div>
</section>

<section class="page page--left">
  <svg class="section-head" style="left:0" width="200" height="34" viewBox="0 0 200 34">
    <rect x="0" y="0" width="41" height="34" fill="var(--teal)"/>
    <polygon points="41,0 164,0 180,17 164,34 41,34 56,17" fill="var(--blue)"/>
    <polygon points="174,0 182,0 198,17 182,34 174,34 190,17" fill="var(--blue)"/>
    <text x="13" y="23" font-size="13">01</text>
    <text x="65" y="23" font-size="13.5">GYMNASTICS</text>
  </svg>

  <div class="photo photo--blue" role="img" aria-label="Photo of a blue crash mat" style="left:21px;top:76px;width:145px;height:60px"></div>
  <article class="card" style="left:174px;top:66px;width:171px;height:83px">
    <h3>Super Soft “Crash” Mats</h3>
    <div class="dims">3600mm x 1800mm x 300mm</div>
    <ul>
      <li>Made locally from the highest quality foam</li>
      <li>6 reinforced handles for easy dependable use</li>
      <li>Reinforced corners for tough school environments</li>
      <li>Military grade zippers</li>
      <li>“rip stop” vinyl to reduce tear propagation</li>
    </ul>
  </article>

  <article class="card card--right" style="left:21px;top:178px;width:165px;height:84px">
    <h3>The Huggy Chair</h3>
    <p>These chairs are being used in classrooms, created for students with autism spectrum conditions and provides a deep, calming pressure as well as core support. This has been found to assist with children’s focus and engagement in class.</p>
  </article>
  <div class="photo photo--red" role="img" aria-label="Photo of a foam huggy chair" style="left:229px;top:188px;width:96px;height:68px"></div>

  <div class="photo photo--red" role="img" aria-label="Photo of a wiggle chair" style="left:70px;top:276px;width:70px;height:92px"></div>
  <article class="card card--center" style="left:21px;top:378px;width:164px;height:72px">
    <h3>The Wiggle Chair</h3>
    <p>Made in our Northby factory, the “Wiggle Chair” has a rounded base to allow for moderate movement and multiple density foam core with a rip stop vinyl cover that is soft, but tough enough to withstand the classroom environment.</p>
  </article>
  <p class="footnote" style="left:21px;top:454px;width:160px">Classroom research notes that many children with sensory needs focus better when gentle movement is allowed. Seating that lets students rock, wiggle and shift their weight helps build core strength, release energy quietly and keep attention on learning tasks for longer periods across the whole school day.</p>

  <div class="photo photo--blue" role="img" aria-label="Photo of a folding wedge mat" style="left:225px;top:295px;width:113px;height:62px"></div>
  <div class="label" style="left:223px;top:372px;width:117px">Folding Wedge</div>
  <div class="photo photo--blue" role="img" aria-label="Photo of a folding incline wedge" style="left:225px;top:408px;width:112px;height:50px"></div>
  <div class="label" style="left:223px;top:468px;width:117px">Folding Wedge2</div>

  <div class="band">sales@vaultasports.com.au</div>
</section>

<section class="page page--right">
  <svg class="section-head" style="left:174px" width="197" height="34" viewBox="0 0 197 34">
    <polygon points="24,0 16,0 0,17 16,34 24,34 8,17" fill="var(--blue)"/>
    <polygon points="36,0 158,0 143,17 158,34 36,34 20,17" fill="var(--blue)"/>
    <rect x="156" y="0" width="41" height="34" fill="var(--teal)"/>
    <text x="38" y="23" font-size="13.5">GYMNASTICS</text>
    <text x="167" y="23" font-size="13">02</text>
  </svg>

  <div class="photo photo--multi" role="img" aria-label="Photo of foam split logs" style="left:41px;top:88px;width:129px;height:42px"></div>
  <div class="label" style="left:41px;top:134px;width:129px">Split Logs</div>

  <div class="label" style="left:214px;top:88px;text-align:left;line-height:1.25">Foam Floor<br>Beam 360x</div>
  <div class="photo photo--purple" role="img" aria-label="Photo of a purple floor beam" style="left:290px;top:78px;width:50px;height:30px"></div>
  <div class="photo photo--multi" role="img" aria-label="Photo of a multi-coloured floor beam" style="left:218px;top:116px;width:44px;height:36px"></div>
  <div class="beam-caption" style="left:266px;top:137px">Floor beam<br>1 piece</div>
  <div class="abs" style="left:304px;top:137px;width:1px;height:16px;background:#333"></div>
  <div class="beam-caption" style="left:310px;top:137px">Floor beam<br>3 pieces</div>

  <div class="photo photo--green" role="img" aria-label="Photo of green foam ninja obstacle pieces" style="left:22px;top:188px;width:140px;height:72px"></div>
  <article class="card card--ninja" style="left:180px;top:174px;width:168px;height:100px">
    <h3>NINJA</h3>
    <div class="ninja-sub">COMPLETE NINJA SYSTEMS</div>
    <p>Our Ninja Systems are a complete set designed for preschool through elementary age students. Pieces in the Ninja System can be easily rearranged to create a multitude of Ninja courses to keep your students engaged.</p>
    <div class="ninja-sub2">BUILD YOUR OWN NINJA SYSTEM</div>
    <p>Each piece of our Ninja System is also available individually, allowing you to configure a system that is ideal for your gym. Add additional components to your existing system or create a totally custom course.</p>
  </article>

  <div class="photo photo--multi" role="img" aria-label="Photo of two trapezoid foam vault boxes" style="left:37px;top:316px;width:122px;height:68px"></div>
  <div class="desc" style="left:20px;top:394px;width:166px;text-align:justify">
    <h3 style="text-align:center">Foam Vault Box</h3>
    Furnish any gym or school with the Trapezoid Foam Vaulting Box to provide students with a fun way to work on motor skills, jumping capabilities and beginner gymnastic manoeuvres. Vaults can be performed seamlessly with the box acting as a horse, or the box can be used as a spotting platform for gymnasts and cheerleaders as they take to the air. Held tightly together by hook-and-loop fasteners, each of the unit’s four sections is bright in colour to add vibrancy to any athletic setting.
  </div>

  <div class="photo photo--dark" role="img" aria-label="Photo of a mini trampoline" style="left:206px;top:306px;width:136px;height:95px"></div>
  <div class="desc" style="left:200px;top:412px;width:148px">
    <h3>Mini Trampoline</h3>
    Strong tubular powder coated frame Adjustable height (quick pin system) Folding legs for easy storage Tough and easy to clean rip stop vinyl padding Lightest folding mini tramp on the market.
  </div>

  <div class="band band--right">www.vaultasports.com.au</div>
</section>

</body>
</html>
```